Face cream packaging | Cosmetic start-up

This project is about creating design proposals for two different types of packaging. Once to a cream jar made of glass and once to a jar made of plastic.
Three different designs must be created for each type of jar. Later, the different packaging will be used as customization options in an online store for cosmetics.

- The packaging variant made of glass should have color gradients. Three different shades are to be chosen. (Preferably with the primary colors red, blue and green). Note: The designer can create other proposals at will if he has better ideas. The logo must be included in some form. (Link to manufacturer description: https://catalogue.valdorpackaging.com/en/portals/valdorpackaging/assets/12667188/lou-50-ml/)

- With the plastic type of packaging, the designer has a lot of freedom to design. The only requirement is that the design must be artistic. It doesn't matter whether abstract patterns, geometric figures, mandalas or just a basic color is chosen. The main thing is that the packaging inspires. The logo must be included in some form. (Link to manufacturer description: https://catalogue.valdorpackaging.com/en/portals/valdorpackaging/assets/12667181/edda-50-ml/)

Thank you in advance for your work and best regards
Olaf

Target Market(s)

Young people with an affinity for social media and the web. Focus is on the female clientele.

Industry/Entity Type

Cosmetics

Font styles to use
Script

Colors
eea4c8
f59195
85cae6
cadf82

Requirements
Must have
• The logo must be included in some form. (PNG-File attached)
Nice to have
• Other types of packaging (can shape, packaging material)

```html
<!DOCTYPE html>
<html lang="en">
<head>
<meta charset="utf-8">
<title>Sela Cosmetics – Cream Label Proposals</title>
<link href="https://fonts.googleapis.com/css2?family=Josefin+Sans:wght@300&family=Open+Sans:wght@400&family=Libre+Franklin:wght@400;700;800&display=swap" rel="stylesheet">
<style>
  :root{
    --stage:#3a3a3a;
    --letter:#c9c9c9;
    --ink:#222222;
    --white:#ffffff;
    --cream:#f3eee0;
    --mint:#d3e8d3;
    --peach:#f9d0c0;
    --salmon:#f2a188;
    --navy:#13284c;
    --blush:#fbe3e3;
    --teal:#9fb8b4;
    --apricot:#f0c4a4;
    --lavender:#ddd8e8;
    --mauve:#ddb3ba;
    --plum:#7a2a5a;
  }
  *{margin:0;padding:0;box-sizing:border-box}
  html,body{width:1200px;height:1086px;overflow:hidden;background:var(--stage)}
  .board{position:relative;width:1200px;height:1086px}
  .variant-letter{
    position:absolute;left:50px;width:60px;text-align:center;
    font-family:"Open Sans",sans-serif;font-size:76px;color:var(--letter);line-height:1;
  }
  .label{position:absolute;left:147px;width:989px;height:198px;overflow:hidden;background:var(--white)}
  .label-bg{position:absolute;inset:0;width:989px;height:198px}
  .copy{
    position:absolute;left:34px;top:26px;width:261px;
    font-family:"Open Sans",sans-serif;font-size:8.6px;line-height:12px;
    color:var(--ink);text-align:justify;text-align-last:justify;
  }
  .copy span{text-align-last:left}
  .code-box{position:absolute;left:34px;top:128px;width:102px;height:54px;background:#050505}
  .brand{
    position:absolute;left:396px;top:54px;width:220px;text-align:center;
    font-family:"Josefin Sans",sans-serif;font-weight:300;font-size:27px;
    color:var(--ink);letter-spacing:1px;white-space:nowrap;
  }
  .brand-rule{position:absolute;left:422px;top:115px;width:168px;height:1px;background:var(--ink)}
  .product{
    position:absolute;left:420px;top:133px;width:170px;text-align:center;
    font-family:"Josefin Sans",sans-serif;font-weight:300;font-size:22px;
    letter-spacing:1.5px;color:var(--ink);
  }
  .nutrition{
    position:absolute;left:725px;top:17px;width:220px;background:var(--white);
    border:1px solid #333;padding:2px 2px 2px 2px;
    font-family:"Libre Franklin",sans-serif;color:#000;
  }
  .nutrition h3{font-weight:800;font-size:12.2px;line-height:13px;white-space:nowrap;letter-spacing:-.2px}
  .nf-small{font-size:5px;line-height:6px}
  .nf-row{display:flex;justify-content:space-between;font-size:5px;line-height:6.4px}
  .nf-row.bold{font-weight:700}
  .nf-row.sub{padding-left:7px}
  .nf-thick{height:4px;background:#000;margin:1px 0}
  .nf-mid{height:2px;background:#000;margin:1px 0}
  .nf-thin{height:1px;background:#000;margin:.5px 0}
  .nf-cal{display:flex;justify-content:space-between;font-weight:800;font-size:10px;line-height:11px}
  .nf-cal b{font-size:12px}
  .nf-right{text-align:right;font-size:3.6px;font-weight:700;line-height:5px}
  .nf-foot{font-size:3.6px;line-height:4.6px;margin-top:1px}
  .claim{
    position:absolute;left:727px;top:152px;width:240px;
    font-family:"Open Sans",sans-serif;font-size:7.6px;line-height:10px;color:var(--ink);
  }
  .label-b .product{left:460px;top:133px;color:var(--white)}
  .label-b .claim{color:var(--white)}
</style>
</head>
<body>
<main class="board">

  <!-- Variant A -->
  <div class="variant-letter" style="top:176px">A</div>
  <section class="label label-a" style="top:96px">
    <svg class="label-bg" viewBox="0 0 989 198" role="img" aria-label="Faint pastel pattern of scattered leaves and sprigs on white">
      <defs>
        <linearGradient id="leafTint" x1="0" y1="0" x2="1" y2="1">
          <stop offset="0" stop-color="#f7f3f1"/>
          <stop offset=".5" stop-color="#f9faf6"/>
          <stop offset="1" stop-color="#f8f0ee"/>
        </linearGradient>
      </defs>
      <rect width="989" height="198" fill="url(#leafTint)"/>
    </svg>
    <div class="label-content">
      <p class="copy">Lorem ipsum dolor sit amet, consectetuer adipiscing elit, sed diam nonummy nibh euismod tincidunt ut laoreet dolore magna aliquam erat volutpat. Ut wisi enim ad minim veniam, quis nostrud exerci tation ullamcorper suscipit lobortis nisl ut aliquip ex ea commodo consequat. Duis autem vel eum iriure dolor in hendrerit in vulputate velit esse molestie consequat, vel illum dolore eu feugiat nulla facilisis at vero eros et <span>luptatum zzril delenit augue duis dolore te feugait nulla facilisi.</span></p>
      <div class="code-box"></div>
      <div class="brand">sela cosmetics</div>
      <div class="brand-rule"></div>
      <div class="product">CREAM</div>
      <div class="nutrition">
        <h3>Nutrition Facts/Datos de Nutrición</h3>
        <div class="nf-small">4 servings per container/6 raciones por envase</div>
        <div class="nf-row bold"><span>Serving size/Tamaño de la porción</span><span>1 cup/1 taza (180g)</span></div>
        <div class="nf-thick"></div>
        <div class="nf-small" style="font-size:3.6px;line-height:4px;font-weight:700">Amount per serving/Cantidad por porción</div>
        <div class="nf-cal"><span>Calories/Calorías</span><b>245</b></div>
        <div class="nf-mid"></div>
        <div class="nf-right">% Daily Value*/% Valor diario*</div>
        <div class="nf-thin"></div>
        <div class="nf-row bold"><span>Total Fat/Grasa total 12g</span><span>14%</span></div>
        <div class="nf-row sub"><span>Saturated Fat/Grasa Saturada 2g</span><span><b>10%</b></span></div>
        <div class="nf-row sub"><span><i>Trans Fat/Grasa Trans 0g</i></span><span></span></div>
        <div class="nf-row bold"><span>Cholesterol/Colesterol 8mg</span><span>3%</span></div>
        <div class="nf-row bold"><span>Sodium/Sodio 210mg</span><span>9%</span></div>
        <div class="nf-row bold"><span>Total Carbohydrate/Carbohidrato Total 34g</span><span>12%</span></div>
        <div class="nf-mid"></div>
        <div class="nf-foot">*Daily Value shows how much a nutrient in a serving adds to a daily diet.<br>*Valor Diario indica cuánto aporta un nutriente a una dieta diaria.</div>
      </div>
      <p class="claim">Lorem ipsum amet, consectetuer adipiscing elit,<br>tincidunt ut laoreet dolore magna aliquam erat volutpat.</p>
    </div>
  </section>

  <!-- Variant B -->
  <div class="variant-letter" style="top:408px">B</div>
  <section class="label label-b" style="top:328px">
    <svg class="label-bg" viewBox="0 0 989 198" aria-hidden="true">
      <rect width="989" height="198" fill="var(--cream)"/>
      <path d="M0,0 H420 C470,50 420,120 470,150 C510,175 520,190 505,198 H0 Z" fill="var(--peach)"/>
      <path d="M0,0 H440 C360,10 390,90 330,120 C270,150 130,130 0,140 Z" fill="var(--mint)"/>
      <path d="M620,0 H989 V50 C930,62 880,40 840,52 C780,62 720,52 680,32 C650,16 632,6 620,0 Z" fill="var(--salmon)"/>
      <path d="M410,198 C470,170 560,140 620,135 C700,130 760,160 830,130 C880,110 940,50 989,15 V198 Z" fill="var(--navy)"/>
    </svg>
    <div class="label-content">
      <p class="copy">Lorem ipsum dolor sit amet, consectetuer adipiscing elit, sed diam nonummy nibh euismod tincidunt ut laoreet dolore magna aliquam erat volutpat. Ut wisi enim ad minim veniam, quis nostrud exerci tation ullamcorper suscipit lobortis nisl ut aliquip ex ea commodo consequat. Duis autem vel eum iriure dolor in hendrerit in vulputate velit esse molestie consequat, vel illum dolore eu feugiat nulla facilisis at vero eros et <span>luptatum zzril delenit augue duis dolore te feugait nulla facilisi.</span></p>
      <div class="code-box"></div>
      <div class="brand">sela cosmetics</div>
      <div class="brand-rule"></div>
      <div class="product">CREAM</div>
      <div class="nutrition">
        <h3>Nutrition Facts/Datos de Nutrición</h3>
        <div class="nf-small">4 servings per container/6 raciones por envase</div>
        <div class="nf-row bold"><span>Serving size/Tamaño de la porción</span><span>1 cup/1 taza (180g)</span></div>
        <div class="nf-thick"></div>
        <div class="nf-small" style="font-size:3.6px;line-height:4px;font-weight:700">Amount per serving/Cantidad por porción</div>
        <div class="nf-cal"><span>Calories/Calorías</span><b>245</b></div>
        <div class="nf-mid"></div>
        <div class="nf-right">% Daily Value*/% Valor diario*</div>
        <div class="nf-thin"></div>
        <div class="nf-row bold"><span>Total Fat/Grasa total 12g</span><span>14%</span></div>
        <div class="nf-row sub"><span>Saturated Fat/Grasa Saturada 2g</span><span><b>10%</b></span></div>
        <div class="nf-row sub"><span><i>Trans Fat/Grasa Trans 0g</i></span><span></span></div>
        <div class="nf-row bold"><span>Cholesterol/Colesterol 8mg</span><span>3%</span></div>
        <div class="nf-row bold"><span>Sodium/Sodio 210mg</span><span>9%</span></div>
        <div class="nf-row bold"><span>Total Carbohydrate/Carbohidrato Total 34g</span><span>12%</span></div>
        <div class="nf-mid"></div>
        <div class="nf-foot">*Daily Value shows how much a nutrient in a serving adds to a daily diet.<br>*Valor Diario indica cuánto aporta un nutriente a una dieta diaria.</div>
      </div>
      <p class="claim">Lorem ipsum amet, consectetuer adipiscing elit,<br>tincidunt ut laoreet dolore magna aliquam erat volutpat.</p>
    </div>
  </section>

  <!-- Variant C -->
  <div class="variant-letter" style="top:640px">C</div>
  <section class="label label-c" style="top:560px">
    <svg class="label-bg" viewBox="0 0 989 198" aria-hidden="true">
      <rect width="989" height="198" fill="var(--blush)"/>
      <path d="M0,0 H280 C292,20 270,40 230,40 C180,40 150,60 140,90 C120,110 40,110 0,100 Z" fill="var(--teal)"/>
      <path d="M0,122 C80,118 200,112 300,124 C335,136 322,180 292,198 H0 Z" fill="var(--apricot)"/>
      <path d="M540,198 C590,150 680,110 760,110 C850,110 900,150 989,150 V198 Z" fill="var(--lavender)"/>
      <path d="M770,0 H989 V62 C920,42 860,42 780,12 Z" fill="var(--mauve)"/>
      <g role="img" aria-label="Cluster of small dark scattered dots">
        <rect x="162" y="122" width="100" height="66" rx="30" fill="#d9b09a"/>
      </g>
      <g role="img" aria-label="Fine line-art contour rings">
        <ellipse cx="470" cy="170" rx="90" ry="40" fill="#f6d9db"/>
        <ellipse cx="640" cy="26" rx="80" ry="26" fill="#f8e4e6"/>
      </g>
      <g role="img" aria-label="Teal leafy plant sprig">
        <rect x="652" y="86" width="64" height="112" rx="28" fill="#b9cbcb"/>
      </g>
    </svg>
    <div class="label-content">
      <p class="copy">Lorem ipsum dolor sit amet, consectetuer adipiscing elit, sed diam nonummy nibh euismod tincidunt ut laoreet dolore magna aliquam erat volutpat. Ut wisi enim ad minim veniam, quis nostrud exerci tation ullamcorper suscipit lobortis nisl ut aliquip ex ea commodo consequat. Duis autem vel eum iriure dolor in hendrerit in vulputate velit esse molestie consequat, vel illum dolore eu feugiat nulla facilisis at vero eros et <span>luptatum zzril delenit augue duis dolore te feugait nulla facilisi.</span></p>
      <div class="code-box"></div>
      <div class="brand">sela cosmetics</div>
      <div class="brand-rule"></div>
      <div class="product">CREAM</div>
      <div class="nutrition">
        <h3>Nutrition Facts/Datos de Nutrición</h3>
        <div class="nf-small">4 servings per container/6 raciones por envase</div>
        <div class="nf-row bold"><span>Serving size/Tamaño de la porción</span><span>1 cup/1 taza (180g)</span></div>
        <div class="nf-thick"></div>
        <div class="nf-small" style="font-size:3.6px;line-height:4px;font-weight:700">Amount per serving/Cantidad por porción</div>
        <div class="nf-cal"><span>Calories/Calorías</span><b>245</b></div>
        <div class="nf-mid"></div>
        <div class="nf-right">% Daily Value*/% Valor diario*</div>
        <div class="nf-thin"></div>
        <div class="nf-row bold"><span>Total Fat/Grasa total 12g</span><span>14%</span></div>
        <div class="nf-row sub"><span>Saturated Fat/Grasa Saturada 2g</span><span><b>10%</b></span></div>
        <div class="nf-row sub"><span><i>Trans Fat/Grasa Trans 0g</i></span><span></span></div>
        <div class="nf-row bold"><span>Cholesterol/Colesterol 8mg</span><span>3%</span></div>
        <div class="nf-row bold"><span>Sodium/Sodio 210mg</span><span>9%</span></div>
        <div class="nf-row bold"><span>Total Carbohydrate/Carbohidrato Total 34g</span><span>12%</span></div>
        <div class="nf-mid"></div>
        <div class="nf-foot">*Daily Value shows how much a nutrient in a serving adds to a daily diet.<br>*Valor Diario indica cuánto aporta un nutriente a una dieta diaria.</div>
      </div>
      <p class="claim">Lorem ipsum amet, consectetuer adipiscing elit,<br>tincidunt ut laoreet dolore magna aliquam erat volutpat.</p>
    </div>
  </section>

  <!-- Variant D -->
  <div class="variant-letter" style="top:872px">D</div>
  <section class="label label-d" style="top:792px">
    <svg class="label-bg" viewBox="0 0 989 198" aria-hidden="true">
      <defs>
        <linearGradient id="washTone" x1="0" y1="0" x2="1" y2="0">
          <stop offset="0" stop-color="#e7c3d0"/>
          <stop offset=".3" stop-color="#f4d3d3"/>
          <stop offset=".48" stop-color="#f2b8b6"/>
          <stop offset=".62" stop-color="#f8eeee"/>
          <stop offset="1" stop-color="#f3c9cf"/>
        </linearGradient>
        <radialGradient id="roseTone" cx=".5" cy=".5" r=".5">
          <stop offset="0" stop-color="#e2b4c6"/>
          <stop offset="1" stop-color="#e2b4c6" stop-opacity="0"/>
        </radialGradient>
      </defs>
      <g role="img" aria-label="Soft pink watercolour wash">
        <rect width="989" height="198" fill="url(#washTone)"/>
      </g>
      <g role="img" aria-label="Plum line-art rose with stems and leaves">
        <ellipse cx="790" cy="100" rx="220" ry="120" fill="url(#roseTone)"/>
      </g>
    </svg>
    <div class="label-content">
      <p class="copy">Lorem ipsum dolor sit amet, consectetuer adipiscing elit, sed diam nonummy nibh euismod tincidunt ut laoreet dolore magna aliquam erat volutpat. Ut wisi enim ad minim veniam, quis nostrud exerci tation ullamcorper suscipit lobortis nisl ut aliquip ex ea commodo consequat. Duis autem vel eum iriure dolor in hendrerit in vulputate velit esse molestie consequat, vel illum dolore eu feugiat nulla facilisis at vero eros et <span>luptatum zzril delenit augue duis dolore te feugait nulla facilisi.</span></p>
      <div class="code-box"></div>
      <div class="brand">sela cosmetics</div>
      <div class="brand-rule"></div>
      <div class="product">CREAM</div>
      <div class="nutrition">
        <h3>Nutrition Facts/Datos de Nutrición</h3>
        <div class="nf-small">4 servings per container/6 raciones por envase</div>
        <div class="nf-row bold"><span>Serving size/Tamaño de la porción</span><span>1 cup/1 taza (180g)</span></div>
        <div class="nf-thick"></div>
        <div class="nf-small" style="font-size:3.6px;line-height:4px;font-weight:700">Amount per serving/Cantidad por porción</div>
        <div class="nf-cal"><span>Calories/Calorías</span><b>245</b></div>
        <div class="nf-mid"></div>
        <div class="nf-right">% Daily Value*/% Valor diario*</div>
        <div class="nf-thin"></div>
        <div class="nf-row bold"><span>Total Fat/Grasa total 12g</span><span>14%</span></div>
        <div class="nf-row sub"><span>Saturated Fat/Grasa Saturada 2g</span><span><b>10%</b></span></div>
        <div class="nf-row sub"><span><i>Trans Fat/Grasa Trans 0g</i></span><span></span></div>
        <div class="nf-row bold"><span>Cholesterol/Colesterol 8mg</span><span>3%</span></div>
        <div class="nf-row bold"><span>Sodium/Sodio 210mg</span><span>9%</span></div>
        <div class="nf-row bold"><span>Total Carbohydrate/Carbohidrato Total 34g</span><span>12%</span></div>
        <div class="nf-mid"></div>
        <div class="nf-foot">*Daily Value shows how much a nutrient in a serving adds to a daily diet.<br>*Valor Diario indica cuánto aporta un nutriente a una dieta diaria.</div>
      </div>
      <p class="claim">Lorem ipsum amet, consectetuer adipiscing elit,<br>tincidunt ut laoreet dolore magna aliquam erat volutpat.</p>
    </div>
  </section>

</main>
</body>
</html>
```